Full service meeting planning company needs new business cards

Velmora Linkway is a full service meeting planning company that specializes in on-line conference registration web development and event communications. We combine citywide hotel management, mobile applications, eblast reminders, confirmation letters, and customized reporting to create a seamless registration process. We also manage group motor coach transportation, food and beverages, entertainment, stage and lighting for group of 10 to 4000.

Target Market(s)

Corporations and associations

Industry/Entity Type

Event Planning

Contact Information for Business Card

standard size 3.5" wide and 2" tall

Font styles to use
Serif
Sans Serif

Colors
f37122
f78f20
333333
5c5c5c
9d9d9d
f68d4d

Requirements
Must have
• {name}
• Velmora Linkway
• P.O. Box 7384, Grand Rapids, M I 49568
• www.velmoralinkway.com
• {email}
• {phone}
• {mobile phone}
Nice to have
• Our colors are black, grey and orange as an accent color
Should not have
• I am not happy with our website layout anymore either. It feels dark and old but it does explain who we are pretty well if you'd like to review; www.velmoralinkway.com

```html
<!DOCTYPE html>
<html lang="en">
<head>
<meta charset="utf-8">
<title>Velmora Linkway — Business Cards</title>
<link href="https://fonts.googleapis.com/css2?family=Montserrat:wght@400;500;700&display=swap" rel="stylesheet">
<style>
  :root {
    --bg: #2b2b2b;
    --card: #050505;
    --orange: #f37122;
    --orange-soft: #f78f20;
    --white: #ffffff;
    --grey: #9d9d9d;
  }
  * { margin: 0; padding: 0; box-sizing: border-box; }
  html, body { width: 1200px; height: 900px; overflow: hidden; }
  body {
    background: var(--bg);
    font-family: "Montserrat", sans-serif;
    position: relative;
  }
  .card {
    position: absolute;
    left: 285px;
    width: 630px;
    height: 360px;
    background: var(--card);
    border-radius: 18px;
    overflow: hidden;
    color: var(--white);
  }
  .card--front { top: 60px; }
  .card--back { top: 480px; }
  .card__bands { position: absolute; inset: 0; width: 100%; height: 100%; }

  /* Front */
  .wordmark {
    position: absolute;
    top: 110px; left: 0; right: 0;
    display: flex; align-items: center; justify-content: center; gap: 18px;
  }
  .wordmark__dot { width: 56px; height: 56px; border-radius: 50%; background: var(--orange); }
  .wordmark__name { font-weight: 700; font-size: 34px; letter-spacing: 1px; color: var(--white); }
  .front__web {
    position: absolute; right: 34px; top: 250px;
    font-size: 17px; font-weight: 500;
  }
  .accent { color: var(--orange); }

  /* Back */
  .back__title {
    position: absolute; left: 36px; top: 42px;
    font-weight: 700; font-size: 50px; letter-spacing: 1.5px; text-transform: uppercase;
  }
  .back__rule {
    position: absolute; left: 170px; right: 30px; top: 118px;
    height: 2px; background: var(--white);
  }
  .person { position: absolute; right: 34px; top: 130px; text-align: right; }
  .person__name { color: var(--orange); font-weight: 700; font-size: 24px; }
  .person__role { font-size: 13px; margin-top: 2px; }
  .address { position: absolute; right: 34px; top: 190px; text-align: right; font-size: 14px; line-height: 1.4; }
  .contacts {
    position: absolute; left: 30px; top: 226px;
    border-top: 1.5px solid var(--white);
    padding-top: 8px; width: 300px;
    list-style: none; font-size: 14px; line-height: 1.45;
  }
  .contacts li { display: flex; align-items: center; gap: 10px; }
  .contacts svg { width: 12px; height: 12px; flex: none; }
</style>
</head>
<body>

<section class="card card--front" aria-label="Business card front">
  <svg class="card__bands" viewBox="0 0 630 360" aria-hidden="true">
    <polygon points="0,290 440,290 500,306 630,306 630,320 500,320 500,360 0,360" fill="var(--orange)"/>
    <polygon points="500,306 630,306 630,320 500,320" fill="var(--white)"/>
  </svg>
  <div class="wordmark">
    <span class="wordmark__dot"></span>
    <span class="wordmark__name">Velmora Linkway</span>
  </div>
  <p class="front__web">www.<span class="accent">velmoralinkway</span>.com</p>
</section>

<section class="card card--back" aria-label="Business card back">
  <svg class="card__bands" viewBox="0 0 630 360" aria-hidden="true">
    <polygon points="452,232 630,232 630,316 432,316" fill="var(--orange)"/>
    <polygon points="240,318 432,318 432,332 228,332" fill="var(--white)"/>
  </svg>
  <h1 class="back__title">Velmora Linkway</h1>
  <div class="back__rule"></div>
  <div class="person">
    <p class="person__name">Marlen Ostrow</p>
    <p class="person__role">Director</p>
  </div>
  <p class="address">P.O. Box 7384<br>Grand Rapids, M I 49568</p>
  <ul class="contacts">
    <li>
      <svg viewBox="0 0 12 12"><path d="M2 1l2 0 1 3-1.5 1a6 6 0 0 0 3.5 3.5L8 7l3 1v2a1 1 0 0 1-1 1A9 9 0 0 1 1 2a1 1 0 0 1 1-1z" fill="var(--orange)"/></svg>
      <span>(616) 555-0142</span>
    </li>
    <li>
      <svg viewBox="0 0 12 12"><rect x="3" y="0.5" width="6" height="11" rx="1" fill="none" stroke="var(--orange)" stroke-width="1.4"/><circle cx="6" cy="9.3" r="0.8" fill="var(--orange)"/></svg>
      <span>(616) 555-0187</span>
    </li>
    <li>
      <svg viewBox="0 0 12 12"><rect x="0.7" y="2.2" width="10.6" height="7.6" fill="none" stroke="var(--orange)" stroke-width="1.4"/><path d="M1 2.5l5 4 5-4" fill="none" stroke="var(--orange)" stroke-width="1.4"/></svg>
      <span>info@velmoralinkway.com</span>
    </li>
    <li>
      <svg viewBox="0 0 12 12"><circle cx="6" cy="6" r="5.2" fill="none" stroke="var(--orange)" stroke-width="1.4"/><path d="M1 6h10M6 1c-2.5 3-2.5 7 0 10M6 1c2.5 3 2.5 7 0 10" fill="none" stroke="var(--orange)" stroke-width="1"/></svg>
      <span>www.<span class="accent">velmoralinkway</span>.com</span>
    </li>
  </ul>
</section>

</body>
</html>
```